Website Design for recruiting company

We need a homepage mockup for a recruiting company focused on the legal industry. Use your creative talent to come up with something visually appeal and professional for this web-site.

We'd really like to see the maze from the logo incorporated into the design somehow. Please use the website mockup provided as inspiration for this project. We really like the layout and photos!

Target Market(s)

lawyers

Industry/Entity Type

Legal

Number of Pages Required

1 page

Font styles to use
Sans Serif

```html
<!DOCTYPE html>
<html lang="en">
<head>
<meta charset="utf-8">
<title>Harbor Crest Legal Search</title>
<link href="https://fonts.googleapis.com/css2?family=Fredoka:wght@600&family=Mulish:wght@200;300;400;600;700;800&display=swap" rel="stylesheet">
<style>
:root{
  --plum:#7a6b7d;
  --plum-dark:#6f6174;
  --plum-deep:#5d5064;
  --sage:#dfe3da;
  --cream:#e7eadf;
  --ink:#2e2b2f;
  --text:#6e6a70;
  --footer:#3f3b41;
  --white:#ffffff;
}
*{box-sizing:border-box;margin:0;padding:0}
html,body{width:1200px;height:3026px;overflow:hidden}
body{position:relative;font-family:"Mulish",sans-serif;background:var(--white);color:var(--ink)}
.abs{position:absolute}
.btn{position:absolute;display:flex;align-items:center;justify-content:center;gap:8px;border-radius:30px;font-family:"Mulish",sans-serif;font-weight:600;font-size:14px;text-transform:uppercase;letter-spacing:.2px}
.btn .dot{width:12px;height:12px;border-radius:50%;background:currentColor;display:inline-block;position:relative}
.btn .dot::after{content:"";position:absolute;left:3px;top:3px;border-left:5px solid var(--dotbg,#fff);border-top:3px solid transparent;border-bottom:3px solid transparent}
.btn-cream{background:var(--cream);color:var(--ink);--dotbg:var(--cream)}
.btn-ghost{border:2px solid var(--cream);color:var(--white);--dotbg:var(--plum-deep)}
.btn-plum{background:var(--plum);color:var(--white);--dotbg:var(--plum)}
.brand{position:absolute;display:flex;align-items:center;gap:12px;color:var(--white);font-weight:300;font-size:16px}
.brand .mark{width:94px;height:94px;border-radius:50%;background:var(--cream)}
/* hero */
.hero{position:absolute;left:0;top:0;width:1200px;height:792px;background:linear-gradient(100deg,#8a7d8c 0%,#6d6072 45%,#4a4150 70%,#3b3540 100%)}
.nav{position:absolute;top:58px;left:583px;display:flex;gap:24px;color:var(--white);font-weight:600;font-size:14px}
.nav .active{border-bottom:2px solid var(--white);padding-bottom:8px}
.search-icon{position:absolute;left:1025px;top:51px;width:31px;height:31px;border-radius:50%;background:var(--cream)}
.hero h1{position:absolute;left:143px;top:293px;font-family:"Fredoka",sans-serif;font-weight:600;font-size:80px;color:var(--cream);line-height:1}
.hero h2{position:absolute;left:143px;top:388px;font-family:"Fredoka",sans-serif;font-weight:600;font-size:40px;color:var(--white)}
.hero p{position:absolute;left:144px;top:467px;width:560px;font-size:14px;line-height:26px;color:var(--white);font-weight:600}
.scroll{position:absolute;left:588px;top:709px}
/* search band */
.jobband{position:absolute;left:0;top:792px;width:1200px;height:122px;background:var(--plum)}
.jobband h3{position:absolute;left:143px;top:42px;font-family:"Fredoka",sans-serif;font-weight:600;font-size:26px;color:var(--white)}
.field{position:absolute;top:41px;width:213px;height:39px;background:var(--white);font-size:13px;color:#555;padding:12px 22px}
.field-btn{position:absolute;left:891px;top:41px;width:165px;height:39px;background:var(--cream);display:flex;align-items:center;justify-content:center;gap:8px;font-size:14px;font-weight:600;--dotbg:var(--cream)}
/* about */
.about-photo{position:absolute;left:140px;top:983px;width:416px;height:416px;border-radius:50%;background:radial-gradient(circle,#d9dadf 0%,#b9bcc4 55%,#8d8c94 100%)}
.about h2{position:absolute;left:600px;top:998px;font-size:48px;font-weight:800;color:var(--ink)}
.about h3{position:absolute;left:599px;top:1048px;font-size:40px;font-weight:200;color:var(--plum-deep)}
.about p{position:absolute;left:600px;top:1125px;width:460px;font-size:15px;line-height:28px;color:var(--text)}
/* whats new */
.news-title{position:absolute;left:0;width:1200px;top:1568px;text-align:center;font-size:48px;color:var(--ink)}
.news-title b{font-weight:800}.news-title span{font-weight:200}
.card{position:absolute;background:var(--white);height:228px;padding:30px 24px;box-shadow:0 2px 8px rgba(0,0,0,.06)}
.card h4{font-size:16px;font-weight:600;text-transform:uppercase;line-height:20px;color:var(--ink)}
.card .date{font-size:13px;color:#666;margin-top:10px}
.card .id{display:inline-block;background:var(--plum);color:var(--white);font-size:14px;font-weight:600;padding:3px 12px;margin-top:16px}
.card p{font-size:12px;line-height:21px;color:#8a8690;margin-top:16px;height:63px;overflow:hidden}
.card .plus{position:absolute;right:0;bottom:0;width:38px;height:32px;background:var(--plum);border-radius:32px 0 0 0;color:var(--white);font-weight:700;font-size:20px;text-align:center;line-height:34px;padding-left:6px}
/* split */
.split h2{position:absolute;top:2460px;font-family:"Fredoka",sans-serif;font-weight:600;font-size:48px;color:var(--white)}
.split p{position:absolute;top:2537px;width:400px;font-size:15px;line-height:28px;color:var(--white)}
.split .btn{font-size:13px;height:45px;top:2686px}
/* footer */
.footer{position:absolute;left:0;top:2843px;width:1200px;height:183px;background:var(--footer);color:var(--white)}
.footer .social{position:absolute;top:80px;left:693px;display:flex;gap:26px}
.footer .social span{width:18px;height:18px;border-radius:50%;background:var(--white);display:block}
.footer .contact{position:absolute;left:943px;top:80px;font-size:14px;font-weight:700;display:flex;align-items:center;gap:8px;--dotbg:var(--footer)}
.footer .copy{position:absolute;left:0;width:1200px;top:130px;text-align:center;font-size:12px}
</style>
</head>
<body>

<section class="hero" role="img" aria-label="Photo of a thoughtful lawyer at a desk across from a colleague, tinted plum">
</section>
<div class="brand" style="left:144px;top:20px"><span class="mark"></span>harbor crest legal search</div>
<nav class="nav"><span class="active">HOME</span><span>ABOUT US</span><span>WHAT’S NEW</span><span>FOR EMPLOYERS</span></nav>
<div class="search-icon"><svg width="31" height="31"><circle cx="14" cy="14" r="5" fill="none" stroke="#3b353f" stroke-width="2"/><line x1="18" y1="18" x2="21" y2="21" stroke="#3b353f" stroke-width="2"/></svg></div>
<div class="hero">
  <h1>Start Here,</h1>
  <h2>Let Our Experience Guide You</h2>
  <p>Lorem ipsum dolor sit amet, consectetur adipiscing elit, sed do eiusmod tempor incididunt ut labore et dolore magna aliquis ipsum suspendisse ultrices gravida. Risus commodo viverra maecenas accumsan lacus vel facilisis.</p>
  <a class="btn btn-cream" style="left:144px;top:589px;width:274px;height:51px">Find the right candidate <i class="dot"></i></a>
  <a class="btn btn-ghost" style="left:426px;top:589px;width:177px;height:51px">Start here <i class="dot"></i></a>
  <svg class="scroll" width="24" height="52"><rect x="2" y="2" width="20" height="30" rx="10" fill="none" stroke="#fff" stroke-width="2"/><line x1="12" y1="9" x2="12" y2="15" stroke="#fff" stroke-width="2"/><polyline points="4,40 12,48 20,40" fill="none" stroke="#fff" stroke-width="2"/></svg>
</div>

<section class="jobband">
  <h3>Find your perfect job.</h3>
  <div class="field" style="left:436px">Job Title</div>
  <div class="field" style="left:664px">State or City<svg class="abs" style="right:12px;top:17px" width="10" height="6"><polygon points="0,0 10,0 5,6" fill="#333"/></svg></div>
  <div class="field-btn">SEARCH JOBS <i class="btn dot" style="position:relative;width:12px;height:12px;border-radius:50%;background:#2e2b2f"></i></div>
</section>

<section class="about">
  <div class="about-photo" role="img" aria-label="Circular photo of a team meeting in an office"></div>
  <h2>ABOUT</h2>
  <h3>Harbor Crest Legal Search</h3>
  <p>Harbor Crest Legal Search focuses on the permanent placement of attorneys with law firms and corporations in the New England area. Founded in 1982, Harbor Crest Legal Search is the oldest attorney search firm in New England, and is ranked the number one legal recruiter in New England in the most recent survey conducted by The Counsel Review.</p>
  <a class="btn btn-plum" style="left:600px;top:1325px;width:160px;height:50px">Read more <i class="dot"></i></a>
</section>

<svg class="abs" style="left:0;top:1460px" width="1200" height="940">
  <path d="M0 85 Q600 -40 1200 85 L1200 825 Q600 925 0 825 Z" fill="var(--sage)"/>
</svg>
<div class="abs" style="left:0;top:2285px;width:600px;height:558px;background:var(--plum)"></div>
<div class="abs" style="left:600px;top:2285px;width:600px;height:558px;background:var(--plum-dark)"></div>
<svg class="abs" style="left:0;top:2270px" width="1200" height="120">
  <path d="M0 15 Q600 115 1200 15 L1200 0 L0 0 Z" fill="var(--sage)"/>
  <circle cx="600" cy="83" r="51" fill="var(--sage)"/>
  <circle cx="600" cy="83" r="37" fill="#6f6174"/>
</svg>

<h2 class="news-title"><b>WHAT’S</b> <span>NEW</span></h2>
<article class="card" style="left:144px;top:1667px;width:289px">
  <h4>In-House/Corporate/M&amp;A</h4><div class="date">Listing Date: 02/10/2020</div><span class="id">JOB ID: 2772</span>
  <p>Global Keystone Exchange medical technology leader seeks 8+ year M&amp;A specialist with major law firm training for lead role</p><span class="plus">+</span>
</article>
<article class="card" style="left:456px;top:1667px;width:289px">
  <h4>Associate/Litigation</h4><div class="date">Listing Date: 02/04/2020</div><span class="id">JOB ID: 2778</span>
  <p>Highly regarded mid-size national firm seeks litigation associate with 4-8 years of experience to join their Litigation Practice.</p><span class="plus">+</span>
</article>
<article class="card" style="left:767px;top:1667px;width:289px">
  <h4>In-House/Senior Corporate Counsel/Securities</h4><div class="date">Listing Date: 02/10/2020</div><span class="id">JOB ID: 2768</span>
  <p style="height:42px">Leading Cambridge-based Keystone Exchange biotechnology company seeks 10+ year</p><span class="plus">+</span>
</article>
<article class="card" style="left:144px;top:1921px;width:443px">
  <h4>In-House/Biotech/Contracts</h4><div class="date">Listing Date: 01/28/2020</div><span class="id">JOB ID: 2777</span>
  <p>Outstanding opportunity for 3+ year attorney to join a premier biotech company in contracts counsel role. Prior experience drafting and negotiating biotech agreements</p><span class="plus">+</span>
</article>
<article class="card" style="left:613px;top:1921px;width:443px">
  <h4>In-House/Corporate/Life Sciences Technology Incubator</h4><div class="date">Listing Date: 01/28/2020</div><span class="id">JOB ID: 2777</span>
  <p style="height:42px">Leading university research group seeks corporate attorney to serve as lead counsel for their life science technology incubator. Qualified</p><span class="plus">+</span>
</article>
<a class="btn btn-plum" style="left:512px;top:2200px;width:176px;height:50px">Search jobs <i class="dot"></i></a>

<section class="split">
  <h2 style="left:142px">LAW FIRMS</h2>
  <p style="left:144px">Lorem ipsum dolor sit amet, consectetur adipiscing elit, sed do eiusmod tempor incididunt ut labore et dolore magna aliqua. Quis ipsum suspendisse ultrices gravida. Risus commodo viverra maecenas accumsan lacus vel facilisis.</p>
  <a class="btn btn-cream" style="left:144px;width:242px">Find the right candidate <i class="dot"></i></a>
  <a class="btn btn-ghost" style="left:394px;width:157px;--dotbg:var(--plum)">Start here <i class="dot"></i></a>
  <h2 style="left:647px">IN HOUSE</h2>
  <p style="left:650px">Lorem ipsum dolor sit amet, consectetur adipiscing elit, sed do eiusmod tempor incididunt ut labore et dolore magna aliqua. Quis ipsum suspendisse ultrices gravida. Risus commodo viverra maecenas accumsan lacus vel facilisis.</p>
  <a class="btn btn-cream" style="left:650px;width:242px">Find the right candidate <i class="dot"></i></a>
  <a class="btn btn-ghost" style="left:900px;width:157px;--dotbg:var(--plum-dark)">Start here <i class="dot"></i></a>
</section>

<footer class="footer">
  <div class="brand" style="left:146px;top:38px"><span class="mark"></span>harbor crest legal search</div>
  <div class="abs" style="left:445px;top:89px;width:220px;height:1px;background:#5a555c"></div>
  <div class="social"><span></span><span></span><span></span><span></span><span></span></div>
  <div class="contact">CONTACT US <i class="btn dot" style="position:relative;width:12px;height:12px;border-radius:50%;background:#fff"></i></div>
  <div class="copy">© 2020 Harbor Crest Legal Search . All rights reserved.</div>
</footer>

</body>
</html>
```